Retro game shop business card design

We need a card designed both front and back. we already have a logo. The business name is called Brisk Copper Atlas and we work on customizing and modifying old velmora zuma tabs. Our website is briskcopperatlas.com

our business cards are often shown in glintly posts ans should be designed so that you can easy identify and see in am image. @briskcopperatlas.

Target Market(s)

men 13-40

Contact Information for Business Card

should have logo, wesbite, and if possible some artwork related to zuma tab mods

Font styles to use
Sans Serif

Colors

Designer to choose colors to be used in the design.

Requirements
Must have
• logo, website url www.briskcopperatlas.com, hastag #zumatabmods, email, support@briskcopperatlas.com. zuma tab imagry only (illustration preffered)
Nice to have
• illustrations, graphic design with zuma tab mods (see glintly #zumatabmods)
Should not have
• childlike depictions of zumatabs, kids, anything unrelated to zuma tab mods, no hands, no bertil, no pixel art

```html
<!DOCTYPE html>
<html lang="en">
<head>
<meta charset="utf-8">
<title>Brisk Copper Atlas – Business Card</title>
<link href="https://fonts.googleapis.com/css2?family=Lato:wght@400;700;900&display=swap" rel="stylesheet">
<style>
  :root {
    --page-bg: #2b2b2d;
    --card-bg: #b4b4b5;
    --logo-grey: #7c7c7d;
    --brand-blue: #4a62b8;
    --text-grey: #5f5f61;
    --art-light: #e9eaee;
    --art-mid: #8e96b8;
    --art-dark: #4a4a4d;
  }
  * { margin: 0; padding: 0; box-sizing: border-box; }
  html, body {
    width: 1200px; height: 900px; overflow: hidden;
    background: var(--page-bg);
    font-family: "Lato", sans-serif;
  }
  .canvas { position: relative; width: 1200px; height: 900px; }
  .card {
    position: absolute; left: 290px; width: 620px; height: 354px;
    background: var(--card-bg); border-radius: 18px; overflow: hidden;
  }
  .card--back { top: 80px; }
  .card--front { top: 466px; }

  .brand-mark {
    position: absolute; left: 150px; top: 120px;
    display: flex; align-items: center; gap: 16px;
  }
  .brand-mark__square { width: 34px; height: 34px; background: var(--logo-grey); }
  .brand-mark__name {
    font-weight: 900; font-size: 40px; line-height: 1.05;
    color: var(--logo-grey); text-transform: uppercase; letter-spacing: 1px;
  }

  .person__name {
    position: absolute; left: 40px; top: 106px;
    font-weight: 700; font-size: 28px; color: var(--brand-blue); letter-spacing: 0.5px;
  }
  .person__title {
    position: absolute; left: 40px; top: 142px;
    font-size: 17px; color: var(--text-grey);
  }
  .address {
    position: absolute; left: 66px; top: 188px;
    font-size: 15px; line-height: 21px; color: var(--text-grey);
  }
  .contact-list {
    position: absolute; left: 40px; top: 238px; list-style: none;
  }
  .contact-list li {
    display: flex; align-items: center; gap: 10px;
    height: 24px; font-size: 15px; color: var(--text-grey);
  }
  .contact-list svg { width: 16px; height: 16px; fill: none; stroke: var(--brand-blue); stroke-width: 1.6; }
  .accent { color: var(--brand-blue); }
  .hashtag {
    position: absolute; left: 40px; top: 318px;
    font-size: 16px; color: var(--brand-blue);
  }
  .mascot-art {
    position: absolute; left: 400px; top: 36px; width: 180px; height: 270px;
    border-radius: 16px;
    background: linear-gradient(160deg, var(--art-light) 0%, var(--art-mid) 45%, var(--art-light) 70%, var(--art-dark) 100%);
  }
</style>
</head>
<body>
<main class="canvas">
  <section class="card card--back" aria-label="Card back">
    <div class="brand-mark">
      <span class="brand-mark__square"></span>
      <span class="brand-mark__name">Brisk Copper<br>Atlas</span>
    </div>
  </section>

  <section class="card card--front" aria-label="Card front">
    <h1 class="person__name">DANA REYES</h1>
    <p class="person__title">Founder &amp; CEO</p>
    <p class="address">1234 First Line Address<br>5678 Second Line Address</p>
    <ul class="contact-list">
      <li>
        <svg viewBox="0 0 16 16"><path d="M4 2l2 3-1.5 1.5a8 8 0 0 0 5 5L11 10l3 2-1.5 2.5C7 14 2 9 1.5 3.5z"/></svg>
        1234567890
      </li>
      <li>
        <svg viewBox="0 0 16 16"><rect x="1.5" y="3.5" width="13" height="9"/><path d="M1.5 3.5L8 9l6.5-5.5"/></svg>
        support@briskcopperatlas.com
      </li>
      <li>
        <svg viewBox="0 0 16 16"><circle cx="8" cy="8" r="6.5"/><path d="M1.5 8h13M8 1.5c-3 3.5-3 9.5 0 13M8 1.5c3 3.5 3 9.5 0 13"/></svg>
        <span>www.<span class="accent">briskcopperatlas</span>.com</span>
      </li>
    </ul>
    <p class="hashtag">#zumatabmods</p>
    <div class="mascot-art" role="img" aria-label="Illustration of a dapper handheld console mascot with top hat and cane"></div>
  </section>
</main>
</body>
</html>
```